Everything fresh, everything new

When I take over the practice, I would like to breathe new life into the practice. I want a business card design that catches the eye and brings a breath of fresh air

```html
<!DOCTYPE html>
<html lang="de">
<head>
<meta charset="utf-8">
<title>Praxis Lindgrün – Visitenkarte</title>
<link rel="stylesheet" href="https://fonts.googleapis.com/css2?family=Montserrat:wght@400;500;700;800&display=swap">
<style>
  :root {
    --stage: #1f1f21;
    --card: #4a4a4d;
    --green: #8cc63f;
    --white: #ffffff;
    --muted: #e9e9e9;
  }
  * { box-sizing: border-box; margin: 0; padding: 0; }
  html, body { width: 1200px; height: 996px; overflow: hidden; }
  body {
    background: var(--stage);
    font-family: "Montserrat", Arial, sans-serif;
    position: relative;
  }
  .card {
    position: absolute;
    top: 165px;
    width: 380px;
    height: 666px;
    background: var(--card);
    border-radius: 24px;
    overflow: hidden;
    box-shadow: 0 18px 40px rgba(0,0,0,.45);
  }
  .card--front { left: 170px; }
  .card--back { left: 650px; }
  .card__footer-band {
    position: absolute;
    left: 0; right: 0; bottom: 0;
    height: 20px;
    background: var(--green);
  }
  .brand {
    position: absolute;
    left: 0; right: 0;
    display: flex;
    flex-direction: column;
    align-items: center;
  }
  .card--front .brand { top: 232px; }
  .card--back .brand { top: 84px; }
  .brand__row { display: flex; align-items: center; gap: 10px; }
  .brand__dot {
    width: 18px; height: 18px;
    border-radius: 50%;
    background: var(--green);
  }
  .brand__name {
    color: var(--white);
    font-weight: 700;
    font-size: 34px;
    letter-spacing: .5px;
  }
  .brand__tagline {
    margin-top: 8px;
    color: var(--muted);
    font-size: 12px;
    font-weight: 500;
    letter-spacing: .6px;
  }
  .name-band {
    position: absolute;
    left: 0; right: 0;
    top: 262px;
    height: 110px;
    background: var(--green);
    color: var(--white);
    text-align: center;
    padding-top: 26px;
  }
  .name-band__name {
    font-weight: 800;
    font-size: 30px;
    letter-spacing: 3px;
  }
  .name-band__role {
    font-weight: 400;
    font-size: 17px;
    letter-spacing: 2px;
    margin-top: 2px;
  }
  .divider {
    position: absolute;
    left: 0; right: 0;
    display: flex;
    align-items: center;
    justify-content: center;
    gap: 8px;
  }
  .divider__line { width: 78px; height: 1px; background: var(--green); }
  .divider__icons { display: flex; gap: 8px; padding: 0 6px; }
  .icon {
    width: 26px; height: 26px;
    border-radius: 50%;
    background: var(--green);
    display: flex; align-items: center; justify-content: center;
  }
  .divider--contact { top: 398px; }
  .divider--address { top: 534px; }
  .contact, .address {
    position: absolute;
    left: 0; right: 0;
    text-align: center;
    color: var(--white);
    font-size: 16px;
    line-height: 1.6;
    letter-spacing: .8px;
  }
  .contact { top: 434px; }
  .address { top: 570px; font-size: 15px; line-height: 1.5; }
</style>
</head>
<body>

<section class="card card--front">
  <div class="brand">
    <div class="brand__row">
      <span class="brand__dot"></span>
      <span class="brand__name">Praxis Lindgrün</span>
    </div>
    <span class="brand__tagline">Neue Wege zur Gesundheit</span>
  </div>
  <div class="card__footer-band"></div>
</section>

<section class="card card--back">
  <div class="brand">
    <div class="brand__row">
      <span class="brand__dot"></span>
      <span class="brand__name">Praxis Lindgrün</span>
    </div>
    <span class="brand__tagline">Neue Wege zur Gesundheit</span>
  </div>

  <div class="name-band">
    <p class="name-band__name">JONAS WEBER</p>
    <p class="name-band__role">MANAGER</p>
  </div>

  <div class="divider divider--contact">
    <span class="divider__line"></span>
    <div class="divider__icons">
      <span class="icon" aria-label="Telefon">
        <svg width="14" height="14" viewBox="0 0 24 24"><path fill="#fff" d="M6.6 10.8a15 15 0 0 0 6.6 6.6l2.2-2.2a1 1 0 0 1 1-.25 11.4 11.4 0 0 0 3.6.57 1 1 0 0 1 1 1V20a1 1 0 0 1-1 1A17 17 0 0 1 3 4a1 1 0 0 1 1-1h3.5a1 1 0 0 1 1 1c0 1.25.2 2.45.57 3.6a1 1 0 0 1-.25 1z"/></svg>
      </span>
      <span class="icon" aria-label="E-Mail">
        <svg width="14" height="14" viewBox="0 0 24 24"><rect x="3" y="6" width="18" height="12" rx="1" fill="#fff"/><path d="M3 6l9 7 9-7" fill="none" stroke="#8cc63f" stroke-width="1.6"/></svg>
      </span>
      <span class="icon" aria-label="Web">
        <svg width="14" height="14" viewBox="0 0 24 24" fill="none" stroke="#fff" stroke-width="2"><circle cx="12" cy="12" r="9"/><path d="M3 12h18M12 3c3 3 3 15 0 18M12 3c-3 3-3 15 0 18"/></svg>
      </span>
    </div>
    <span class="divider__line"></span>
  </div>

  <div class="contact">
    <p>555.014.2290</p>
    <p>hallo@lindgruen-praxis.de</p>
    <p>www.lindgruen-praxis.de</p>
  </div>

  <div class="divider divider--address">
    <span class="divider__line"></span>
    <div class="divider__icons">
      <span class="icon" aria-label="Adresse">
        <svg width="14" height="14" viewBox="0 0 24 24"><path fill="#fff" d="M12 2a7 7 0 0 0-7 7c0 5 7 13 7 13s7-8 7-13a7 7 0 0 0-7-7zm0 9.5A2.5 2.5 0 1 1 12 6.5a2.5 2.5 0 0 1 0 5z"/></svg>
      </span>
    </div>
    <span class="divider__line"></span>
  </div>

  <div class="address">
    <p>42 Birkenallee</p>
    <p>Musterstadt, 10115</p>
  </div>

  <div class="card__footer-band"></div>
</section>

</body>
</html>
```